Design some Business Cards for Tavro

Thanks to everyone for their efforts. I will just be reviewing the first two entries from each contestant, so I'd suggest withdrawing entries which are not your favorites & going with your best two. Many thanks, Derek

I was after a double sided business card for tavro.com.au. Tavro is a billing app and website for tradesman and service providers who move from site to site.

Firstly design for Derek Holm with mobile 0481 555 907 & email demo@tavro.com.au.

Logo is attached, so please work with those colours. I've also included our url if you believe that is worth building in.

I would like the original working files and the business card will need to be produced for 3 different employees when the winner is selected.

Additional TAVRO text files if this helps.

```html
<!DOCTYPE html>
<html lang="en">
<head>
<meta charset="utf-8">
<title>Tavro Business Cards</title>
<link rel="stylesheet" href="https://fonts.googleapis.com/css2?family=Lato:wght@400;700;900&display=swap">
<style>
  :root {
    --backdrop: #ece9e4;
    --card: #ffffff;
    --ink: #141414;
    --band: #0b0b0b;
    --accent: #1b9fd9;
    --soft-grey: #dcdde0;
    --mark-red: #d8322b;
    --muted: #3a3a3a;
  }
  * { margin: 0; padding: 0; box-sizing: border-box; }
  html, body {
    width: 1200px; height: 901px; overflow: hidden;
    background: var(--backdrop);
    font-family: "Lato", sans-serif;
  }
  .stage { position: relative; width: 1200px; height: 901px; }
  .card {
    position: absolute; width: 620px; height: 354px;
    background: var(--card); overflow: hidden;
    box-shadow: 0 6px 18px rgba(0,0,0,0.18);
  }
  .card--front { left: 80px; top: 70px; }
  .card--back { left: 500px; top: 477px; }

  .brand { position: absolute; display: flex; align-items: center; gap: 14px; }
  .brand__dot {
    border-radius: 50%; border: 3px solid var(--mark-red);
  }
  .brand__name { font-weight: 900; color: var(--ink); letter-spacing: 3px; line-height: 1; }

  .card--front .brand { left: 150px; top: 88px; }
  .card--front .brand__dot { width: 70px; height: 70px; }
  .card--front .brand__name { font-size: 62px; }

  .front-band {
    position: absolute; left: 0; right: 0; bottom: 0; height: 100px;
    background: var(--band); border-top: 7px solid var(--accent);
    display: flex; align-items: center; justify-content: center;
  }
  .front-band__url { color: #fff; font-size: 19px; letter-spacing: 1.5px; }

  .back-topbar { position: absolute; left: 0; right: 0; top: 0; height: 26px; background: var(--soft-grey); }
  .card--back .brand { right: 28px; top: 48px; }
  .card--back .brand__dot { width: 50px; height: 50px; }
  .card--back .brand__name { font-size: 44px; }
  .back-rule { position: absolute; left: 300px; right: 20px; top: 118px; height: 2px; background: var(--soft-grey); }

  .back-shape { position: absolute; inset: 0; }

  .person { position: absolute; left: 28px; top: 168px; }
  .person__name { font-size: 28px; font-weight: 700; color: var(--accent); }
  .person__role { font-size: 15px; color: var(--muted); margin-top: 4px; }
  .person__rule { width: 186px; height: 3px; background: var(--accent); margin-top: 10px; }

  .contacts { position: absolute; left: 28px; top: 268px; list-style: none; }
  .contacts li { display: flex; align-items: center; gap: 12px; font-size: 14px; color: var(--muted); height: 24px; }
  .contacts svg { width: 13px; height: 13px; fill: #555; }
</style>
</head>
<body>
<main class="stage">
  <section class="card card--front" aria-label="Card front">
    <div class="brand">
      <span class="brand__dot"></span>
      <span class="brand__name">TAVRO</span>
    </div>
    <div class="front-band">
      <span class="front-band__url">WWW.TAVRO.COM.AU</span>
    </div>
  </section>

  <section class="card card--back" aria-label="Card back">
    <div class="back-topbar"></div>
    <svg class="back-shape" viewBox="0 0 620 354" width="620" height="354" aria-hidden="true">
      <polygon points="260,354 620,148 620,354" fill="var(--band)"/>
      <polygon points="248,354 620,141 620,150 262,354" fill="var(--accent)"/>
    </svg>
    <div class="brand">
      <span class="brand__dot"></span>
      <span class="brand__name">TAVRO</span>
    </div>
    <div class="back-rule"></div>
    <div class="person">
      <h1 class="person__name">Derek Holm</h1>
      <p class="person__role">Managing Director</p>
      <div class="person__rule"></div>
    </div>
    <ul class="contacts">
      <li><svg viewBox="0 0 12 12"><path d="M3 0h6a1 1 0 0 1 1 1v10a1 1 0 0 1-1 1H3a1 1 0 0 1-1-1V1a1 1 0 0 1 1-1zm0 2v7h6V2z"/></svg>0481 555 907</li>
      <li><svg viewBox="0 0 12 12"><path d="M0 2h12v8H0zm1 1v.5l5 3 5-3V3z"/></svg>demo@tavro.com.au</li>
      <li><svg viewBox="0 0 12 12"><circle cx="6" cy="6" r="5.5"/></svg>www.tavro.com.au</li>
    </ul>
  </section>
</main>
</body>
</html>
```